PowerPoint design MedoraVix

We need a PowerPoint set-up based upon our existing logo (see joint file)
Our company is operating in the health care and life science sector. We are mainly focussing on international business

Target Market(s)

International

Industry/Entity Type

health care and life sciences

Requirements
Must have
• Logos as added

```html
<!DOCTYPE html>
<html lang="en">
<head>
<meta charset="utf-8">
<title>MedoraVix – Presentation Template</title>
<link href="https://fonts.googleapis.com/css2?family=Inter:ital,wght@0,400;0,500;0,600;0,700;1,400;1,500&display=swap" rel="stylesheet">
<style>
:root{
  --blue:#0b4f8a;
  --blue-deep:#0a4a82;
  --blue-photo:#2a6aa3;
  --green:#5cbf1a;
  --ink:#2f2f2f;
  --muted:#555;
  --page:#e2e2e2;
  --card:#f1f1f1;
  --white:#ffffff;
}
*{box-sizing:border-box;margin:0;padding:0}
html,body{width:1200px;height:1200px;overflow:hidden;background:var(--page);font-family:"Inter",Arial,sans-serif;color:var(--ink)}
.canvas{position:relative;width:1200px;height:1200px}
.slide{position:absolute;width:434px;height:244px;background:var(--white);overflow:hidden}
.col-a{left:147px}.col-b{left:624px}
.row-1{top:69px}.row-2{top:348px}.row-3{top:628px}.row-4{top:907px}
.abs{position:absolute}
.brand{position:absolute;display:flex;align-items:center;gap:5px;font-weight:600;color:var(--blue);white-space:nowrap}
.brand .dot{border-radius:50%;background:var(--blue)}
.brand-sm{left:26px;bottom:9px;font-size:8px}
.brand-sm .dot{width:12px;height:12px}
.brand-md{font-size:11px}
.brand-md .dot{width:17px;height:17px}
.footer-web{position:absolute;right:26px;bottom:10px;display:flex;align-items:center;gap:4px;font-size:4.5px;color:#888}
.footer-web .num{width:12px;height:12px;border-radius:50%;background:var(--green);color:#fff;font-size:5px;display:flex;align-items:center;justify-content:center}
.photo{position:absolute}
.rule{width:16px;height:1.5px;background:var(--green)}
.h-slide{font-weight:700;color:var(--blue);font-size:18px}
.lorem{font-size:8px;line-height:1.33;color:#333}

/* Title slide */
.title-photo{left:200px;top:0;width:234px;height:244px;background:linear-gradient(120deg,#eef2f5 0%,#f7f7f7 40%,#d9dfe4 70%,#c9cfd5 100%)}
.title-panel{left:0;top:0}
.title-text{left:26px;top:76px;color:#fff}
.title-text h1{font-size:21.5px;font-weight:700;line-height:1.25}
.title-text .rule{margin:12px 0 12px}
.title-text p{font-size:10px}

/* Mission */
.mission-band{left:0;top:71px;width:228px;height:51px;background:var(--blue);display:flex;align-items:center;padding-left:20px;gap:10px;color:#fff;font-size:9px;font-weight:600}
.mission-band .ic{width:24px;height:24px;border-radius:50%;background:var(--green);display:flex;align-items:center;justify-content:center}
.mission-copy{left:26px;top:131px;width:172px}
.mission-copy p+p{margin-top:5px}
.mission-photo{left:228px;top:0;width:206px;height:216px;border-bottom-left-radius:34px;background:linear-gradient(135deg,#dfe6ec 0%,#c7d2dc 45%,#aab8c6 100%)}

/* Services */
.svc-top{left:0;top:0;width:434px;height:122px;background:linear-gradient(120deg,#2e6ea6,#23609a 60%,#1f5a93)}
.svc-title{left:0;top:24px;width:434px;text-align:center;color:#fff;font-size:18px;font-weight:700}
.svc-card{top:87px;width:120px;height:122px;background:#fff;box-shadow:0 1px 4px rgba(0,0,0,.12);text-align:center;padding-top:36px}
.svc-card h3{font-size:9px;font-weight:600;color:var(--blue)}
.svc-card .sep{width:12px;height:1px;background:#ddd;margin:8px auto 8px}
.svc-card p{font-size:7.2px;line-height:9.6px;color:#444;padding:0 9px}
.svc-badge{top:64px;width:50px;height:50px}

/* Teams */
.team-title{left:0;top:20px;width:434px;text-align:center}
.team-card{width:122px;height:73px;background:var(--card);padding:8px 8px 0}
.team-head{display:flex;align-items:center;gap:6px}
.avatar{width:18px;height:18px;border-radius:50%;background:var(--blue);position:relative;flex:none}
.team-name{font-size:6.5px;font-weight:600;color:var(--blue)}
.team-pos{font-size:6px;font-style:italic;color:var(--blue)}
.team-line{height:1px;background:var(--green);margin:6px 0 5px}
.team-card p{font-size:5.2px;line-height:6.6px;color:#444}

/* Section */
.sec-band{left:0;top:55px;width:434px;height:189px;background:linear-gradient(110deg,#2d6aa2,#25629b 50%,#1e5890)}
.sec-text{left:26px;top:128px;color:#fff}
.sec-text h2{font-size:18px;font-weight:700}
.sec-text .rule{margin:10px 0 9px}
.sec-text p{font-size:12px}

/* Process */
.proc-title{left:26px;top:22px;color:var(--ink);font-size:18px}
.proc-col{top:120px;width:104px}
.proc-col h4{font-size:10.5px;font-weight:600;color:var(--ink)}
.proc-col .rule{width:12px;height:1px;margin:6px 0 7px}
.proc-col p{font-size:7.1px;line-height:8.7px;color:#444}

/* Chart */
.chart-side{left:0;top:0;width:152px;height:244px;background:linear-gradient(160deg,#2c69a1,#1f5a93)}
.chart-bg{left:152px;top:0;width:282px;height:244px;background:#f1f1f1}
.chart-title{left:26px;top:22px;color:#fff;font-size:17px;font-weight:700;line-height:1.12}
.chart-title .rule{margin-top:7px}
.chart-card{left:120px;top:22px;width:288px;height:191px;background:#fff;border-radius:4px;box-shadow:0 1px 4px rgba(0,0,0,.12)}

/* Contact */
.contact-text{left:26px;top:53px;color:#fff;width:124px}
.contact-text h2{font-size:16px;font-weight:700}
.contact-text .rule{margin:8px 0 16px}
.contact-text p{font-size:9px;line-height:10.9px}
.contact-info{left:241px;top:104px;width:167px;color:var(--blue)}
.contact-info .lbl{font-size:9.5px;font-weight:600}
.contact-info .addr{font-size:9.5px;line-height:1.3}
.contact-info .hr{height:1px;background:#cfe3c0;margin:9px 0 11px}
.contact-row{display:flex;align-items:center;gap:10px;font-size:9.5px;font-weight:600;margin-bottom:9px}
.contact-row .ic{width:16px;height:16px;border-radius:50%;background:var(--green);display:flex;align-items:center;justify-content:center}
</style>
</head>
<body>
<main class="canvas">

  <!-- 1 Title -->
  <section class="slide col-a row-1">
    <div class="photo title-photo" role="img" aria-label="Photo of a doctor in a white coat holding a stethoscope"></div>
    <svg class="abs title-panel" width="434" height="244" viewBox="0 0 434 244">
      <path d="M0 0 H150 A122 122 0 0 1 150 244 H0 Z" fill="var(--blue)"/>
      <path d="M0 9 H148 A113 113 0 0 1 148 235 H0" fill="none" stroke="#fff" stroke-width="1.2"/>
      <circle cx="424" cy="227" r="40" fill="var(--green)"/>
    </svg>
    <div class="brand brand-md" style="right:26px;top:19px"><span class="dot"></span>MedoraVix</div>
    <div class="abs title-text">
      <h1>Presentation title<br>here</h1>
      <div class="rule"></div>
      <p>Type your subtitle here</p>
    </div>
  </section>

  <!-- 2 Mission -->
  <section class="slide col-b row-1">
    <h2 class="abs h-slide" style="left:26px;top:21px">Our Mission</h2>
    <div class="abs mission-band">
      <span class="ic"><svg width="10" height="10" viewBox="0 0 10 10"><rect x="3" y="3" width="4" height="6" fill="#fff"/><rect x="2" y="1" width="6" height="2" fill="#fff"/></svg></span>
      Type your mission here
    </div>
    <div class="abs mission-copy lorem">
      <p>Lorem ipsum dolor sit amet, consectetur adipiscing elit, sed do eiusmod tempor incididunt ut labore et dolore magna aliqua.</p>
      <p>Ut enim ad minim veniam, quis nostrud exercitation ullamco laboris nisi ut aliquip ex ea commodo consequat. Duis aute irure dolor in.</p>
    </div>
    <div class="photo mission-photo" role="img" aria-label="Photo of doctors discussing at a desk with a laptop"></div>
    <div class="brand brand-sm"><span class="dot"></span>MedoraVix</div>
    <div class="footer-web">www.medoravix.com<span class="num">2</span></div>
  </section>

  <!-- 3 Services -->
  <section class="slide col-a row-2">
    <div class="photo svc-top" role="img" aria-label="Blue-tinted medical photo background"></div>
    <h2 class="abs svc-title">Our Services</h2>
    <div class="abs svc-card" style="left:26px"><h3>Service title here</h3><div class="sep"></div><p>Lorem ipsum dolor sit amet, consectetur adipiscing elit, sed do eiusmod tempor incididunt ut labore et dolore magna sit aliqua.</p></div>
    <div class="abs svc-card" style="left:157px"><h3>Service title here</h3><div class="sep"></div><p>Lorem ipsum dolor sit amet, consectetur adipiscing elit, sed do eiusmod tempor incididunt ut labore et dolore magna sit aliqua.</p></div>
    <div class="abs svc-card" style="left:288px"><h3>Service title here</h3><div class="sep"></div><p>Lorem ipsum dolor sit amet, consectetur adipiscing elit, sed do eiusmod tempor incididunt ut labore et dolore magna sit aliqua.</p></div>
    <svg class="abs svc-badge" style="left:61px" viewBox="0 0 50 50"><path d="M0 25 A25 25 0 0 1 50 25 Z" fill="var(--green)"/><circle cx="25" cy="25" r="19" fill="#f0f0f0"/><line x1="19" y1="31" x2="30" y2="20" stroke="var(--green)" stroke-width="2.4" stroke-linecap="round"/><circle cx="31" cy="19" r="2.4" fill="var(--green)"/></svg>
    <svg class="abs svc-badge" style="left:192px" viewBox="0 0 50 50"><path d="M0 25 A25 25 0 0 1 50 25 Z" fill="var(--green)"/><circle cx="25" cy="25" r="19" fill="#f0f0f0"/><g fill="none" stroke="var(--green)" stroke-width="1.2"><circle cx="22" cy="21" r="3"/><circle cx="28" cy="22" r="3"/><circle cx="25" cy="28" r="3"/></g></svg>
    <svg class="abs svc-badge" style="left:323px" viewBox="0 0 50 50"><path d="M0 25 A25 25 0 0 1 50 25 Z" fill="var(--green)"/><circle cx="25" cy="25" r="19" fill="#f0f0f0"/><circle cx="25" cy="25" r="7" fill="var(--green)"/><path d="M25 21 V29 M21 25 H29" stroke="#fff" stroke-width="2"/></svg>
    <div class="brand brand-sm"><span class="dot"></span>MedoraVix</div>
    <div class="footer-web">www.medoravix.com<span class="num">3</span></div>
  </section>

  <!-- 4 Teams -->
  <section class="slide col-b row-2">
    <h2 class="abs h-slide team-title">Our teams</h2>
    <div class="abs team-card" style="left:26px;top:58px"><div class="team-head"><span class="avatar"></span><div><div class="team-name">Name here</div><div class="team-pos">Position here</div></div></div><div class="team-line"></div><p>Lorem ipsum dolor sit amet, consectetur adipiscing elit, sed do eiusmod tempor incididunt ut labore et dolore magna sit aliqua.</p></div>
    <div class="abs team-card" style="left:156px;top:58px"><div class="team-head"><span class="avatar"></span><div><div class="team-name">Name here</div><div class="team-pos">Position here</div></div></div><div class="team-line"></div><p>Lorem ipsum dolor sit amet, consectetur adipiscing elit, sed do eiusmod tempor incididunt ut labore et dolore magna sit aliqua.</p></div>
    <div class="abs team-card" style="left:286px;top:58px"><div class="team-head"><span class="avatar"></span><div><div class="team-name">Name here</div><div class="team-pos">Position here</div></div></div><div class="team-line"></div><p>Lorem ipsum dolor sit amet, consectetur adipiscing elit, sed do eiusmod tempor incididunt ut labore et dolore magna sit aliqua.</p></div>
    <div class="abs team-card" style="left:26px;top:138px"><div class="team-head"><span class="avatar"></span><div><div class="team-name">Name here</div><div class="team-pos">Position here</div></div></div><div class="team-line"></div><p>Lorem ipsum dolor sit amet, consectetur adipiscing elit, sed do eiusmod tempor incididunt ut labore et dolore magna sit aliqua.</p></div>
    <div class="abs team-card" style="left:156px;top:138px"><div class="team-head"><span class="avatar"></span><div><div class="team-name">Name here</div><div class="team-pos">Position here</div></div></div><div class="team-line"></div><p>Lorem ipsum dolor sit amet, consectetur adipiscing elit, sed do eiusmod tempor incididunt ut labore et dolore magna sit aliqua.</p></div>
    <div class="abs team-card" style="left:286px;top:138px"><div class="team-head"><span class="avatar"></span><div><div class="team-name">Name here</div><div class="team-pos">Position here</div></div></div><div class="team-line"></div><p>Lorem ipsum dolor sit amet, consectetur adipiscing elit, sed do eiusmod tempor incididunt ut labore et dolore magna sit aliqua.</p></div>
    <div class="brand brand-sm"><span class="dot"></span>MedoraVix</div>
    <div class="footer-web">www.medoravix.com<span class="num">4</span></div>
  </section>

  <!-- 5 Section -->
  <section class="slide col-a row-3">
    <div class="brand brand-md" style="right:26px;top:19px"><span class="dot"></span>MedoraVix</div>
    <div class="photo sec-band" role="img" aria-label="Blue-tinted photo of a doctor writing on a clipboard"></div>
    <div class="abs sec-text">
      <h2>Section title here</h2>
      <div class="rule"></div>
      <p>Subtitle here</p>
    </div>
  </section>

  <!-- 6 Process -->
  <section class="slide col-b row-3">
    <h2 class="abs h-slide proc-title">Our Process</h2>
    <svg class="abs" style="left:0;top:78px" width="434" height="36" viewBox="0 0 434 36">
      <line x1="0" y1="18" x2="406" y2="18" stroke="var(--green)" stroke-width="2"/>
      <path d="M398 11 L406 18 L398 25" fill="none" stroke="var(--green)" stroke-width="2"/>
      <g><circle cx="42" cy="18" r="16" fill="var(--blue)" stroke="var(--green)" stroke-width="2"/><line x1="36" y1="24" x2="46" y2="14" stroke="#fff" stroke-width="2" stroke-linecap="round"/><circle cx="47" cy="13" r="2" fill="#fff"/></g>
      <g><circle cx="178" cy="18" r="16" fill="var(--blue)" stroke="var(--green)" stroke-width="2"/><g fill="none" stroke="#fff" stroke-width="1.1"><circle cx="176" cy="15" r="2.6"/><circle cx="181" cy="16" r="2.6"/><circle cx="178" cy="21" r="2.6"/></g></g>
      <g><circle cx="315" cy="18" r="16" fill="var(--blue)" stroke="var(--green)" stroke-width="2"/><circle cx="315" cy="18" r="6.5" fill="#fff"/><path d="M315 14.5 V21.5 M311.5 18 H318.5" stroke="var(--blue)" stroke-width="1.8"/></g>
    </svg>
    <div class="abs proc-col" style="left:26px"><h4>Process 1</h4><div class="rule"></div><p>Lorem ipsum dolor sit amet, consectetur adipiscing elit, sed do eiusmod tempor incididunt ut labore et dolore magna aliqua. Ut enim ad minim veniam</p></div>
    <div class="abs proc-col" style="left:163px"><h4>Process 2</h4><div class="rule"></div><p>Lorem ipsum dolor sit amet, consectetur adipiscing elit, sed do eiusmod tempor incididunt ut labore et dolore magna aliqua. Ut enim ad minim veniam</p></div>
    <div class="abs proc-col" style="left:299px"><h4>Process 3</h4><div class="rule"></div><p>Lorem ipsum dolor sit amet, consectetur adipiscing elit, sed do eiusmod tempor incididunt ut labore et dolore magna aliqua. Ut enim ad minim veniam</p></div>
    <div class="brand brand-sm"><span class="dot"></span>MedoraVix</div>
    <div class="footer-web">www.medoravix.com<span class="num">6</span></div>
  </section>

  <!-- 7 Chart -->
  <section class="slide col-a row-4">
    <div class="photo chart-side" role="img" aria-label="Blue-tinted photo of a doctor"></div>
    <div class="abs chart-bg"></div>
    <div class="abs chart-title">Chart<br>Report<div class="rule"></div></div>
    <div class="abs chart-card">
      <svg width="288" height="191" viewBox="0 0 288 191" font-family="Inter, Arial, sans-serif">
        <rect x="12" y="12" width="264" height="18" fill="var(--blue)"/>
        <g fill="#fff" font-size="6.5"><text x="19" y="24">Task Name</text><text x="88" y="24" font-weight="600">Jan</text><text x="136" y="24" font-weight="600">Feb</text><text x="184" y="24" font-weight="600">Mar</text><text x="232" y="24" font-weight="600">Apr</text></g>
        <g stroke="#fff" stroke-width="1"><line x1="84" y1="12" x2="84" y2="30"/><line x1="132" y1="12" x2="132" y2="30"/><line x1="180" y1="12" x2="180" y2="30"/><line x1="228" y1="12" x2="228" y2="30"/></g>
        <rect x="12" y="30" width="72" height="137" fill="#f4f4f4"/>
        <g stroke="#e6e6e6" stroke-width="0.8"><line x1="84" y1="30" x2="84" y2="167"/><line x1="132" y1="30" x2="132" y2="167"/><line x1="180" y1="30" x2="180" y2="167"/><line x1="228" y1="30" x2="228" y2="167"/><line x1="12" y1="57" x2="276" y2="57"/><line x1="12" y1="85" x2="276" y2="85"/><line x1="12" y1="112" x2="276" y2="112"/><line x1="12" y1="140" x2="276" y2="140"/></g>
        <g fill="#222" font-size="6" font-weight="600"><text x="19" y="46">Planning</text><text x="19" y="73">Research</text><text x="19" y="100">Design</text><text x="19" y="128">Implementation</text><text x="19" y="155">Follow up</text></g>
        <rect x="84" y="39" width="30" height="9" fill="var(--green)"/>
        <rect x="114" y="66" width="16" height="9" fill="#dcdcdc"/><rect x="130" y="66" width="40" height="9" fill="var(--green)"/>
        <rect x="170" y="94" width="27" height="9" fill="var(--blue)"/>
        <rect x="197" y="121" width="47" height="9" fill="var(--green)"/>
        <rect x="228" y="149" width="46" height="9" fill="var(--blue)"/>
        <g font-size="4.2" fill="#444"><rect x="29" y="176" width="6" height="6" fill="#dcdcdc"/><text x="39" y="181">Lorem ipsum dolor sit amet</text><rect x="114" y="176" width="6" height="6" fill="var(--green)"/><text x="124" y="181">Lorem ipsum dolor sit amet</text><rect x="199" y="176" width="6" height="6" fill="var(--blue)"/><text x="209" y="181">Lorem ipsum dolor sit amet</text></g>
      </svg>
    </div>
    <div class="footer-web">www.medoravix.com<span class="num">7</span></div>
  </section>

  <!-- 8 Contact -->
  <section class="slide col-b row-4">
    <svg class="abs" style="left:0;top:0" width="434" height="244" viewBox="0 0 434 244">
      <path d="M0 0 H208 Q226 0 222 26 Q200 120 146 244 H0 Z" fill="var(--blue)"/>
      <path d="M192 0 Q208 10 204 36 Q182 126 126 244" fill="none" stroke="#fff" stroke-width="1.2"/>
      <path d="M110 244 Q118 205 148 200 Q170 204 171 228 L171 244 Z" fill="var(--green)"/>
      <path d="M382 244 Q402 198 434 186 V244 Z" fill="#ececec"/>
    </svg>
    <div class="abs contact-text">
      <h2>Contact us</h2>
      <div class="rule"></div>
      <p>Lorem ipsum dolor sit amet, consectetur adipiscing elit, sed do eiusmod tempor incididunt ut labore et dolore magna aliqua.</p>
    </div>
    <div class="brand brand-md" style="right:26px;top:21px"><span class="dot"></span>MedoraVix</div>
    <div class="abs contact-info">
      <div class="lbl">Address</div>
      <div class="addr">ABC Street<br>City &amp; Zip Code</div>
      <div class="hr"></div>
      <div class="contact-row"><span class="ic"><svg width="9" height="7" viewBox="0 0 9 7"><rect x="0.5" y="0.5" width="8" height="6" fill="none" stroke="#fff"/><path d="M0.5 0.5 L4.5 4 L8.5 0.5" fill="none" stroke="#fff"/></svg></span>info@medoravix.com</div>
      <div class="contact-row"><span class="ic"><svg width="9" height="9" viewBox="0 0 9 9"><path d="M2 0.5 L3.5 3 L2.5 4 Q3.5 6 5 6.5 L6 5.5 L8.5 7 L7.5 8.5 Q3 8 0.5 2 Z" fill="#fff"/></svg></span>(555) 014-2387</div>
    </div>
  </section>

</main>
</body>
</html>
```